Kem7Dex Letterhead

Need a new letterhead for my law firm.
IDENTIFYING INFORMATION BELOW:
Ansel T Brightwater III
Attorney at Law
Address: 4832 Tillbury Rd, Ste 250, Dallas, TX 75204
Phone: 866-402-7183
Fax: 469-583-0271
Email: kem@kem7dex.example
Website: www.kem7dex.example

Colors
0054AA
0677BA
7BADD7
CADEEF
E8F1F8

Requirements
Must have
• Logo needs to be on the letterhead, along with identifying information which is included in the project description.

```html
<!DOCTYPE html>
<html lang="en">
<head>
<meta charset="utf-8">
<title>Kem7Dex Letterhead</title>
<link href="https://fonts.googleapis.com/css2?family=Montserrat:wght@400;500;800&display=swap" rel="stylesheet">
<style>
  :root {
    --backdrop: #b4b4b4;
    --paper: #ffffff;
    --ink: #111111;
    --body-ink: #3a3a3a;
    --brand-blue: #1487c9;
    --band-text: #ffffff;
    --sign-tone: #d9d9d9;
  }
  * { box-sizing: border-box; margin: 0; padding: 0; }
  html, body {
    width: 1200px; height: 1200px; overflow: hidden;
    background: var(--backdrop);
    font-family: "Montserrat", sans-serif;
  }
  .letterhead {
    position: absolute; left: 170px; top: 41px;
    width: 860px; height: 1118px;
    background: var(--paper);
    box-shadow: 0 6px 18px rgba(0,0,0,0.18);
  }
  .brand { position: absolute; top: 58px; left: 0; width: 100%; text-align: center; }
  .brand-name {
    font-weight: 800; font-size: 58px; letter-spacing: 6px;
    color: var(--ink); line-height: 1;
  }
  .brand-tagline {
    margin-top: 10px; font-weight: 400; font-size: 25px;
    letter-spacing: 4px; color: var(--ink);
  }
  .letter-body {
    position: absolute; left: 92px; top: 290px; width: 676px;
    color: var(--body-ink);
  }
  .salutation { font-size: 17px; font-weight: 500; color: #2a2a2a; margin-bottom: 36px; }
  .letter-body p.para {
    font-size: 13px; line-height: 21.3px; text-align: justify;
    margin-bottom: 22px; letter-spacing: -0.1px;
  }
  .sender-name { margin-top: 20px; font-size: 17px; font-weight: 500; color: #2a2a2a; }
  .sender-role { font-size: 11.5px; color: #333; }
  .signature {
    margin-top: 36px; width: 196px; height: 62px;
    background: linear-gradient(90deg, var(--sign-tone), #efefef);
    border-radius: 4px;
  }
  .attorney { position: absolute; left: 0; top: 976px; width: 100%; text-align: center; }
  .attorney-name { font-size: 22px; font-weight: 500; color: var(--brand-blue); line-height: 1.1; }
  .attorney-title {
    display: flex; align-items: center; gap: 4px;
    margin-top: 3px; font-size: 15px; color: var(--ink);
  }
  .attorney-title::before, .attorney-title::after {
    content: ""; flex: 1; height: 1.5px; background: var(--brand-blue);
  }
  .contact-band {
    position: absolute; left: 0; bottom: 0; width: 100%; height: 87px;
    background: var(--brand-blue); color: var(--band-text);
    display: flex; flex-direction: column; align-items: center; justify-content: center;
    gap: 6px; font-size: 15px; letter-spacing: 0.3px;
  }
  .contact-row { display: flex; align-items: center; gap: 7px; }
  .contact-item { display: inline-flex; align-items: center; gap: 5px; }
  .contact-item svg { width: 11px; height: 11px; fill: none; stroke: var(--band-text); stroke-width: 2; }
  .contact-item svg.solid { fill: var(--band-text); stroke: none; }
</style>
</head>
<body>
  <main class="letterhead">
    <header class="brand">
      <div class="brand-name">KEM7DEX</div>
      <div class="brand-tagline">MOVE WITH KEM</div>
    </header>

    <section class="letter-body">
      <p class="salutation">Dear sir/Madam,</p>
      <p class="para">Lorem Ipsum is simply dummy text of the printing and typesetting industry. Lorem Ipsum has been the industry's standard dummy text ever since the 1500s, when an unknown printer took a galley of type and scrambled it to make a type specimen book. It has survived not only five centuries, but also the leap into electronic typesetting, remaining essentially unchanged. It was popularised in the 1960s with the release of Typeline</p>
      <p class="para">Contrary to popular belief, Lorem Ipsum is not simply random text. It has roots in a piece of classical Latin literature from 45 BC, making it over 2000 years old. Rowan Pellegrew, a Latin professor at Harrowgate College in Virginia, looked up one of the more obscure Latin words, consectetur, from a Lorem Ipsum passage, and going through the cites of the word in classical literature, discovered the undoubtable source. Lorem Ipsum comes from sections 1.10.32 and 1.10.33 of "de Finibus Bonorum et Malorum" (The Extremes of Good and Evil) by Cassian, written in 45 BC. This book is a treatise on the theory of ethics, very popular during the Renaissance. The first line of Lorem Ipsum, "Lorem ipsum dolor sit amet..", comes from a line in section 1.10.32. typesetting, remaining essentially unchanged. It was popularised in the 1960s with the release of Typeline</p>
      <p class="para">Lorem Ipsum is simply dummy text of the printing and typesetting industry. Lorem Ipsum has been the industry's standard dummy text ever since the 1500s, when an unknown printer took a galley of type and scrambled it to make a type specimen book. It has survived not only five centuries, but also the leap into electronic typesetting, remaining essentially unchanged. It was popularised in the 1960s with the release of Typeline</p>
      <div class="sender-name">Marlow P. Quade, Esq.</div>
      <div class="sender-role">Managing Attorney</div>
      <div class="signature" role="img" aria-label="Handwritten signature"></div>
    </section>

    <div class="attorney">
      <div class="attorney-name">Ansel T Brightwater III</div>
      <div class="attorney-title">Attorney at Law</div>
    </div>

    <footer class="contact-band">
      <div class="contact-row">
        <span class="contact-item">
          <svg viewBox="0 0 12 12" class="solid"><path d="M2.5 1 L4.5 1 L5 3.5 L3.8 4.4 Q4.8 6.8 7.6 8.2 L8.5 7 L11 7.5 L11 9.5 Q10.5 11 9 11 Q1 10 1 2.5 Q1 1 2.5 1 Z"/></svg>
          866-402-7183
        </span>
        <span class="contact-item">
          <svg viewBox="0 0 12 12" class="solid"><rect x="3" y="1" width="6" height="3"/><rect x="1" y="4.5" width="10" height="4.5" rx="1"/><rect x="3" y="8" width="6" height="3"/></svg>
          469-583-0271
        </span>
        <span class="contact-item">
          <svg viewBox="0 0 12 12"><rect x="1" y="2.5" width="10" height="7" rx="1"/><path d="M1.5 3 L6 6.5 L10.5 3"/></svg>
          kem@kem7dex.example
        </span>
        <span class="contact-item">
          <svg viewBox="0 0 12 12" style="stroke-width:1.3"><circle cx="6" cy="6" r="5"/><ellipse cx="6" cy="6" rx="2.2" ry="5"/><path d="M1 6 H11 M2 3.5 H10 M2 8.5 H10"/></svg>
          www.kem7dex.example
        </span>
      </div>
      <div class="contact-row">
        <span class="contact-item">
          <svg viewBox="0 0 12 12" class="solid" style="width:12px;height:13px"><path d="M6 0.5 A4 4 0 0 1 10 4.5 C10 7.5 6 11.5 6 11.5 C6 11.5 2 7.5 2 4.5 A4 4 0 0 1 6 0.5 Z M6 3 A1.5 1.5 0 1 0 6 6 A1.5 1.5 0 1 0 6 3 Z" fill-rule="evenodd"/></svg>
          4832 Tillbury Rd, Ste 250, Dallas, TX 75204
        </span>
      </div>
    </footer>
  </main>
</body>
</html>
```